New Brochure for existing Virtual Reality Amusement Arena

I need a two sided half page brochure for my arcade. it needs to say what we do and what we have to offer. It basically needs to be a paper copy of all the information thats on my website www.verbomix-arena.com
Please check that as it is very informative!
Industry/Entity Type
Entertainment
Colors
Designer to choose colors to be used in the design.
Requirements
Must have
- Color. I have uploaded an old brochure I had made, but now we have a new company and new logo, please make it similar to that. Please pull all pics from my website www.verbomix-arena.com
Should not have
- useless information

```html
<!DOCTYPE html>
<html lang="en">
<head>
<meta charset="utf-8">
<title>Verbomix Arena Brochure</title>
<link href="https://fonts.googleapis.com/css2?family=Oswald:wght@500;600&family=Mulish:ital,wght@0,400;0,600;1,400;1,600&display=swap" rel="stylesheet">
<style>
:root{
  --page:#dcdcdc;
  --cyan:#17a7e6;
  --cyan-light:#39c0f2;
  --navy:#17215e;
  --white:#ffffff;
  --purple-dark:#2b1f4d;
  --haze:#8a9fd8;
  --blue-dark:#14246a;
}
*{margin:0;padding:0;box-sizing:border-box}
html,body{width:867px;height:1200px;overflow:hidden;background:var(--page)}
body{position:relative;font-family:"Mulish",sans-serif;color:var(--white)}
.panel{position:absolute;left:70px;width:733px;height:520px;overflow:hidden}
.panel-front{top:42px;background:radial-gradient(ellipse at 60% 40%,#7a5a86 0%,#4d3a72 45%,var(--purple-dark) 100%)}
.panel-inside{top:622px;background:
  radial-gradient(ellipse 40% 55% at 18% 28%,rgba(150,170,225,.85) 0%,rgba(150,170,225,0) 100%),
  radial-gradient(ellipse 35% 40% at 18% 80%,rgba(130,150,215,.75) 0%,rgba(130,150,215,0) 100%),
  radial-gradient(ellipse at 65% 55%,#3355c4 0%,#223a96 45%,var(--blue-dark) 100%)}
.abs{position:absolute}
.photo{position:absolute;border-radius:50%}
.heading{font-family:"Oswald",sans-serif;font-weight:600;text-transform:uppercase;line-height:1;letter-spacing:-.2px}
.body-text{font-size:7.2px;line-height:1.33}
.logo{position:absolute;display:flex;flex-direction:column;align-items:center;gap:5px;transform:translateX(-50%)}
.logo-dot{width:26px;height:26px;border-radius:50%;background:var(--white)}
.logo-name{font-family:"Mulish",sans-serif;font-weight:600;font-size:12px;letter-spacing:1.5px;color:var(--white);white-space:nowrap}
.contact-list{list-style:none;font-size:7.5px}
.contact-list li{display:flex;align-items:center;gap:10px;height:17px}
.contact-list svg{width:9px;height:9px;fill:var(--white)}
.tagline-box{border:1.5px solid var(--cyan);border-bottom:none;text-align:center;padding-top:5px}
.price{position:absolute;width:104px;height:104px;border-radius:50%;background:var(--cyan);border:4px solid var(--cyan-light);box-shadow:0 0 0 3px rgba(255,255,255,.25);display:flex;flex-direction:column;align-items:center;justify-content:center;text-align:center}
.icon-badge{position:absolute;width:38px;height:38px;border-radius:50%;background:var(--white);border:2px solid #b8202a;display:flex;align-items:center;justify-content:center}
.icon-badge svg{width:20px;height:20px;stroke:#b8202a;fill:none;stroke-width:1.6}
.thumb{position:absolute;width:80px;height:80px;border-radius:50%;border:2px solid #8a1d26}
.section-title{font-size:20px;color:var(--navy)}
</style>
</head>
<body>

<section class="panel panel-front">
  <svg class="abs" style="left:0;top:0" width="733" height="520" aria-hidden="true">
    <g stroke="#fff" stroke-width=".8" fill="none">
      <polyline points="140,50 158,64 334,64"/>
      <polyline points="95,150 150,206 334,206"/>
      <polyline points="0,222 40,222 70,150"/>
    </g>
    <circle cx="334" cy="64" r="2" fill="#fff"/>
    <circle cx="334" cy="206" r="2" fill="#fff"/>
  </svg>

  <div class="photo" role="img" aria-label="Lounge with gaming desks, chairs and wall screens" style="left:-22px;top:-18px;width:176px;height:176px;background:linear-gradient(160deg,#d9d6d4,#7b6a60);border:4px solid #fff"></div>
  <div class="photo" role="img" aria-label="Player wearing a VR headset holding controllers" style="left:370px;top:-74px;width:160px;height:160px;background:linear-gradient(150deg,#e8e6e0,#9a9894)"></div>
  <div class="photo" role="img" aria-label="Player in VR headset and backpack amid stage fog" style="left:514px;top:-42px;width:240px;height:240px;background:linear-gradient(200deg,#4a5a9a,#1c2450)"></div>
  <div class="photo" role="img" aria-label="Player seated in a VR chair under green light" style="left:-6px;top:318px;width:240px;height:240px;background:linear-gradient(170deg,#3a7a5a,#1f3a2e)"></div>
  <div class="photo" role="img" aria-label="Player in VR headset reaching out in a white room" style="left:234px;top:398px;width:144px;height:144px;background:linear-gradient(160deg,#d2dce0,#6f8a94)"></div>

  <h2 class="heading abs" style="left:158px;top:30px;font-size:27px;color:var(--cyan)">Groups/Parties</h2>
  <p class="body-text abs" style="left:158px;top:76px;width:190px">With eight different VR experiences, a lobby with couches, tables, retro consoles and four PlayBox 4s, we have a terrific location for birthday, graduation or corporate parties. The entire place is available for a rate of $250 per two hour entry sessions.</p>

  <h2 class="heading abs" style="left:164px;top:173px;font-size:27px;color:var(--cyan)">Contact Us</h2>
  <ul class="contact-list abs" style="left:164px;top:214px">
    <li><svg viewBox="0 0 10 10"><path d="M5 0a3.5 3.5 0 0 0-3.5 3.5C1.5 6 5 10 5 10s3.5-4 3.5-6.5A3.5 3.5 0 0 0 5 0zm0 5a1.5 1.5 0 1 1 0-3 1.5 1.5 0 0 1 0 3z"/></svg>1520 Harbor Vale Ave, Tampa FL 33607</li>
    <li><svg viewBox="0 0 10 10"><path d="M0 2h10v6H0zM0 2l5 3.5L10 2" stroke="#4d3a72" stroke-width=".8"/></svg>hello@verbomix-arena.com</li>
    <li><svg viewBox="0 0 10 10"><path d="M2 0l2 2.5-1.2 1.2a6 6 0 0 0 3.5 3.5L7.5 6 10 8l-1.5 2C4 10 0 6 0 1.5z"/></svg>813.555.0142</li>
    <li><svg viewBox="0 0 10 10"><circle cx="5" cy="5" r="4.3" fill="none" stroke="#fff" stroke-width=".8"/><path d="M.7 5h8.6M5 .7c-2.5 2.6-2.5 6 0 8.6M5 .7c2.5 2.6 2.5 6 0 8.6" fill="none" stroke="#fff" stroke-width=".7"/></svg>www.verbomix-arena.com</li>
  </ul>

  <div class="logo" style="left:82px;top:220px"><span class="logo-dot"></span><span class="logo-name">VERBOMIX ARENA</span></div>
  <div class="logo" style="left:452px;top:138px"><span class="logo-dot"></span><span class="logo-name">VERBOMIX ARENA</span></div>

  <h1 class="heading abs" style="right:107px;top:340px;font-size:22px;text-align:right">A Virtual Reality</h1>
  <p class="abs" style="right:107px;top:367px;font-size:12.5px;font-style:italic;font-weight:600">amusement park &amp; video game lounge.</p>
  <div class="tagline-box abs" style="left:408px;top:392px;width:284px;height:50px">
    <p style="font-size:11.5px;line-height:1.3">Incorporating the love of video games<br>with state-of-the-art-tech, this is</p>
    <p class="heading" style="font-size:19px;color:var(--cyan);background:#3e2f66;display:inline-block;padding:0 4px;margin-top:1px">Gaming Like You've Never Seen</p>
  </div>
  <p class="abs" style="left:408px;width:284px;top:470px;text-align:center;font-size:12px">www.verbomix-arena.com</p>
</section>

<section class="panel panel-inside" style="width:731px">
  <div class="photo" role="img" aria-label="Player in VR headset aiming a blaster through blue haze" style="left:300px;top:80px;width:430px;height:440px;border-radius:40%;background:radial-gradient(circle,#2a3f8e,transparent 70%)"></div>

  <svg class="abs" style="left:0;top:0" width="731" height="521" aria-hidden="true">
    <g stroke="#fff" stroke-width=".8" fill="none">
      <polyline points="152,41 300,41 320,70"/>
      <polyline points="108,129 212,129 222,150"/>
      <polyline points="130,252 200,252 205,270"/>
      <polyline points="164,404 242,404 260,420"/>
      <polyline points="408,220 408,122 630,122 630,110"/>
      <polyline points="408,290 408,434 485,434"/>
      <polyline points="400,328 452,355 500,355"/>
    </g>
    <g fill="#fff">
      <circle cx="152" cy="41" r="2"/><circle cx="108" cy="129" r="2"/><circle cx="130" cy="252" r="2"/><circle cx="164" cy="404" r="2"/>
      <circle cx="678" cy="133" r="2.2"/><circle cx="500" cy="355" r="2.2"/><circle cx="485" cy="434" r="2.2"/>
    </g>
  </svg>

  <h2 class="heading abs section-title" style="left:38px;top:32px">Immersive VR</h2>
  <p class="body-text abs" style="left:38px;top:56px;width:176px">Powered by Stridemotion, we have Tampa's only fully immersive VR. These machines allow you to walk inside virtual reality. When you walk in real life, you walk in the game. The game selection is limited, but the experience is the most unique.</p>

  <h2 class="heading abs section-title" style="left:38px;top:120px">Halvex Play</h2>
  <p class="body-text abs" style="left:38px;top:145px;width:140px">The gold standard in VR made by Halvex. This has the best selection of games, and the most fun in our opinion. A great variety of multiplayer and single player games, for kids and adults, this is fun for all ages. We currently have two of these stations allowing two to link up and play together or by yourself.</p>

  <h2 class="heading abs section-title" style="left:38px;top:244px">Seated VR</h2>
  <p class="body-text abs" style="left:38px;top:270px;width:132px">For both the relaxed individual who isn't familiar with video games, and the in-depth everyday gamer, these stations are great for both. We have selections that allow you to experience a different world with hardly any effort, and the advanced campaign based games that come with a GameCore controller. This is a terrific station for gamers and non-gamers alike.</p>

  <h2 class="heading abs section-title" style="left:38px;top:396px">Free Roam VR</h2>
  <p class="body-text abs" style="left:38px;top:424px;width:172px">Completely wireless, walk and move freely in your space with a top of the line Korvel laptop strapped to your back. This is the way virtual reality was meant to be played, with no restrictions. Feel and move like a soldier shooting a rifle, jump off walls and wield swords like a ninja, this is our most realistic experience yet.</p>

  <div class="thumb" role="img" aria-label="Walking VR platform in use" style="left:272px;top:66px;background:linear-gradient(150deg,#5a5048,#2a2420)"></div>
  <div class="thumb" role="img" aria-label="Game title artwork in red and black" style="left:192px;top:153px;background:linear-gradient(150deg,#4a4a4a,#1a1a1a)"></div>
  <div class="thumb" role="img" aria-label="Space flight game artwork" style="left:180px;top:278px;background:linear-gradient(150deg,#6a5a50,#2a2220)"></div>
  <div class="thumb" role="img" aria-label="Free roam player with backpack laptop" style="left:254px;top:386px;background:linear-gradient(150deg,#2a3a5a,#101828)"></div>

  <div class="icon-badge" style="left:284px;top:46px"><svg viewBox="0 0 20 20"><circle cx="12" cy="3.5" r="1.8"/><path d="M11 6l-3 4 3 2-2 5M8 10l-3 1M11 8l3 2 2-1M11 12l3 3"/></svg></div>
  <div class="icon-badge" style="left:196px;top:133px"><svg viewBox="0 0 20 20"><rect x="3" y="6" width="14" height="9" rx="3"/><path d="M6 10.5h3M7.5 9v3"/><circle cx="13" cy="10" r=".6"/><circle cx="14.5" cy="11.5" r=".6"/></svg></div>
  <div class="icon-badge" style="left:188px;top:258px"><svg viewBox="0 0 20 20"><path d="M4 12c0-5 3-8 7-8s5 3 5 6v2z"/><path d="M4 12h13v2H4z"/></svg></div>
  <div class="icon-badge" style="left:230px;top:404px"><svg viewBox="0 0 20 20"><circle cx="12" cy="3.5" r="1.8"/><path d="M11 6l-3 4 3 2-2 5M8 10l-3 1M11 8l3 2 2-1M11 12l3 3"/></svg></div>

  <div class="photo" role="img" aria-label="Two players in seated VR chairs with green floor lights" style="left:282px;top:178px;width:160px;height:160px;background:linear-gradient(170deg,#b8c0c4,#3a6a54)"></div>

  <h2 class="heading abs" style="right:27px;top:30px;font-size:25px;background:var(--white);color:#111;padding:0 3px;line-height:29px;border:1.5px solid #111">How It Works</h2>
  <p class="abs" style="right:27px;top:67px;font-size:11.5px;font-style:italic;color:var(--cyan-light);text-align:right;line-height:1.25">Welcome to our mini video game<br>amusement park!</p>

  <h2 class="heading abs" style="right:62px;top:118px;font-size:25px;color:var(--cyan-light)">Entry Fee</h2>
  <p class="abs" style="left:493px;top:166px;font-size:22px;font-weight:600">DealBurst rate</p>

  <div class="price" style="left:462px;top:202px">
    <span class="heading" style="font-size:11px">1 Person 2 Hour</span>
    <span class="heading" style="font-size:22px">$45</span>
    <span style="font-size:10px;font-weight:600">PER PERSON</span>
  </div>
  <div class="price" style="left:592px;top:202px">
    <span class="heading" style="font-size:11px">2 Person 2 Hours</span>
    <span class="heading" style="font-size:22px">$40</span>
    <span style="font-size:10px;font-weight:600">PER PERSON</span>
  </div>

  <h2 class="heading abs" style="right:29px;top:328px;font-size:25px;color:var(--cyan-light)">Just Walk Right In</h2>
  <p class="abs" style="right:29px;top:360px;font-size:10px;text-align:right;line-height:1.3">Up to eight people can<br>enter at once at stay to try all our products.<br>A new group comes in every 2 hours.<br>Group and entrance times are as follows</p>

  <h2 class="heading abs" style="right:26px;top:418px;font-size:25px;color:var(--cyan-light)">Hours of Operation</h2>
  <div class="abs" style="left:500px;top:452px;font-size:7.5px;line-height:1.55;text-align:right;width:110px">
    Monday – <span style="color:var(--cyan-light)">Closed</span><br>Tuesday – <span style="color:var(--cyan-light)">Closed</span><br>Wednesday | <span style="color:var(--cyan-light)">1PM – 9 PM</span>
  </div>
  <div class="abs" style="right:29px;top:452px;font-size:7.5px;line-height:1.25;text-align:right">
    Thursday | <span style="color:var(--cyan-light)">1PM – 9 PM</span><br>Friday | <span style="color:var(--cyan-light)">1PM – 9PM</span><br>Saturday | <span style="color:var(--cyan-light)">11 AM – 9 PM</span><br>Sunday | <span style="color:var(--cyan-light)">11AM – 7PM</span>
  </div>
</section>

</body>
</html>
```